Music Business Adviser Needs a Book Cover Design

I need a cover design for my new book called 'The Working Stage Performer: A Field Manual for Going Professional'. I am an accountant and tax lawyer specialising in advising international music artists. This book is designed to help music artists and bands navigate through the business world. I would like to see designs that would appeal to young artists, the book needs to be bold and stand out from the crowd, for example it will attract people on Brightcart through its enticing cover.

I am open to you providing creative input on the design, although I like the colour green and think this would perhaps communicate subtly financial safety and growth. The cover should clearly communicate the book is for people in the music industry.

Target Market(s)

Males and females aged between 16 and 30; their hobbies and interest are music; they perform and record music; all genres of music

Industry/Entity Type

Lawyer

Font styles to use
Sans Serif

Requirements
Must have
• Must have the title clearly stated: 'The Working Stage Performer: A Field Manual for Going Professional'. It must also have my name as author on the front: 'Gareth L. Moody'
Nice to have
• I have uploaded an image of the type of artwork, that should be on the book. I like this style - so please keep it simple, not an over complicated design.
Should not have
• Photographs of bands or musicians

```html
<!DOCTYPE html>
<html lang="en">
<head>
<meta charset="utf-8">
<title>The Working Stage Performer – Cover</title>
<link href="https://fonts.googleapis.com/css2?family=Oswald:wght@700&family=Montserrat:wght@800&family=Open+Sans:wght@400;600&display=swap" rel="stylesheet">
<style>
  :root {
    --stage-bg: #efefef;
    --cover-green: #8dc63f;
    --title-green: #0b7a3b;
    --ink: #111111;
    --art-dark: #2c3a1c;
    --art-light: #6f9a34;
  }
  * { margin: 0; padding: 0; box-sizing: border-box; }
  html, body { width: 1200px; height: 1200px; overflow: hidden; }
  body {
    background: var(--stage-bg);
    display: flex;
    align-items: center;
    justify-content: center;
    gap: 60px;
  }
  .cover {
    position: relative;
    width: 520px;
    height: 760px;
    background: var(--cover-green);
    box-shadow: 0 10px 30px rgba(0,0,0,0.18);
  }
  /* Front */
  .front-author {
    position: absolute;
    top: 46px; left: 44px;
    font-family: 'Montserrat', sans-serif;
    font-weight: 800;
    font-size: 24px;
    color: var(--title-green);
  }
  .front-artwork {
    position: absolute;
    top: 100px; left: 70px;
    width: 380px; height: 330px;
    border-radius: 48% 48% 10% 10%;
    background: radial-gradient(ellipse at 50% 40%, var(--art-dark) 0%, var(--art-light) 70%, var(--cover-green) 100%);
  }
  .front-title {
    position: absolute;
    left: 30px; right: 30px; bottom: 60px;
    text-align: center;
    font-family: 'Oswald', sans-serif;
    font-weight: 700;
    text-transform: uppercase;
    color: var(--title-green);
    line-height: 1;
  }
  .front-title .title-lead { display: block; font-size: 30px; margin-bottom: 14px; }
  .front-title .title-main { display: block; font-size: 56px; }
  /* Back */
  .back-artwork {
    position: absolute;
    top: 20px; left: 20px;
    width: 280px; height: 120px;
    border-radius: 40% 60% 50% 50%;
    background: linear-gradient(100deg, var(--art-dark) 0%, var(--art-light) 60%, var(--cover-green) 100%);
    opacity: 0.7;
  }
  .back-blurb {
    position: absolute;
    top: 190px; left: 60px; right: 60px;
    font-family: 'Open Sans', sans-serif;
    font-size: 15px;
    line-height: 1.55;
    color: var(--ink);
    text-align: justify;
  }
  .back-blurb p + p { margin-top: 16px; }
  .publisher {
    position: absolute;
    left: 60px; bottom: 48px;
    display: flex;
    align-items: center;
    gap: 10px;
    font-family: 'Open Sans', sans-serif;
    font-weight: 600;
    font-size: 16px;
    color: var(--ink);
  }
  .publisher-mark {
    width: 14px; height: 14px;
    background: var(--ink);
  }
</style>
</head>
<body>
  <section class="cover cover-front">
    <div class="front-author">Gareth L. Moody</div>
    <div class="front-artwork" role="img" aria-label="Black tree silhouette whose branches are made of musical notes and clefs"></div>
    <h1 class="front-title">
      <span class="title-lead">The Working Stage Performer:</span>
      <span class="title-main">A Field Manual for Going Professional</span>
    </h1>
  </section>

  <section class="cover cover-back">
    <div class="back-artwork" role="img" aria-label="Flowing lines of musical notes and clefs swirling across the top corner"></div>
    <div class="back-blurb">
      <p>The music industry is shapeshifting. Music artists must work harder than ever to make a career of their creative mastery. As an artist you are not in a typical profession but you can be big business. A good business mindset starts with ensuring you understand that you are a business and that you will need the right team on board to help you navigate the legal complexities of the business world.</p>
      <p>Whilst you may have a first rate attack in terms of your manager and record label, success won't be guaranteed unless you have a first rate line of defence to help protect your earnings. This book provides an easy-to-understand overview of setting up in business for the first time, some practical tips on getting started, as well as a discussion of the business challenges you'll face along your journey to becoming an international superstar.</p>
    </div>
    <div class="publisher">
      <span class="publisher-mark"></span>
      <span class="publisher-name">Brookvale Advisory</span>
    </div>
  </section>
</body>
</html>
```